Quorvex - Automated robotic Inspection with AI need new business cards

We need a new design of our business cards. The company is focused on automated quality control at high speed with unmatched results. We have a logo but need a more forward leaning business card that shows that we are delivering cutting edge technology.

Contact Information for Business Card

Name
Position
Adress
Phone
Email
e.g.
Lena Holmqvist
Chief Financial Officer (CFO)

Quorvex Sweden AB
Bruksvägen 14, SE-175 43 JÄRFÄLLA, Sweden
Mobile: +46735 21 47 83 | Office: +46 8 61 94 27
www.quorvex-example.com

Font styles to use
Sans Serif

```html
<!DOCTYPE html>
<html lang="en">
<head>
<meta charset="utf-8">
<title>Quorvex Business Card</title>
<link rel="stylesheet" href="https://fonts.googleapis.com/css2?family=Bebas+Neue&family=Libre+Franklin:wght@400;600;700&display=swap">
<style>
  :root {
    --brand-blue: #004f7e;
    --ink: #231f20;
    --paper: #ffffff;
    --swoosh-grey: #b9bbbe;
    --backdrop: #dde8f1;
  }
  * { margin: 0; padding: 0; box-sizing: border-box; }
  html, body { width: 1200px; height: 1200px; overflow: hidden; }
  body {
    background: var(--backdrop);
    position: relative;
    font-family: "Libre Franklin", Arial, sans-serif;
  }
  .card {
    position: absolute;
    left: 283px;
    width: 634px;
    height: 362px;
    overflow: hidden;
  }
  .card--front { top: 174px; background: var(--paper); }
  .card--back { top: 609px; background: var(--brand-blue); }

  .brand-name {
    position: absolute;
    font-family: "Libre Franklin", Arial, sans-serif;
    font-weight: 600;
    letter-spacing: 2px;
    line-height: 1;
  }
  .card--front .brand-name {
    left: 35px; top: 38px;
    font-size: 56px;
    color: var(--brand-blue);
  }
  .card--back .brand-name {
    left: 0; right: 0; top: 139px;
    text-align: center;
    font-size: 84px;
    color: var(--paper);
  }

  .holder {
    position: absolute;
    right: 28px; top: 153px;
    text-align: right;
  }
  .holder__name {
    font-family: "Bebas Neue", Impact, sans-serif;
    font-size: 32px;
    line-height: 1;
    color: var(--brand-blue);
    letter-spacing: 0.2px;
  }
  .holder__role {
    font-size: 16px;
    color: var(--ink);
    margin-top: 2px;
  }
  .holder-accent {
    position: absolute;
    right: 0; top: 153px;
    width: 20px; height: 45px;
    background: var(--brand-blue);
  }

  .contact {
    position: absolute;
    left: 35px; top: 185px;
    font-size: 15.5px;
    line-height: 20px;
    color: var(--ink);
  }
  .contact__company { color: var(--brand-blue); font-weight: 700; }
  .contact__phones { margin-top: 8px; }
  .contact__label {
    display: inline-block;
    width: 60px;
    color: var(--brand-blue);
  }

  .footer-band {
    position: absolute;
    left: 0; bottom: 0;
    width: 634px; height: 62px;
  }
  .web {
    position: absolute;
    left: 35px; top: 329px;
    font-size: 17px;
    letter-spacing: 2px;
    color: var(--paper);
  }
  .web strong { font-weight: 700; }
</style>
</head>
<body>
  <section class="card card--front">
    <div class="brand-name">QUORVEX</div>

    <div class="holder">
      <div class="holder__name">LENA HOLMQVIST</div>
      <div class="holder__role">Chief Financial Officer (CFO)</div>
    </div>
    <div class="holder-accent"></div>

    <div class="contact">
      <div class="contact__company">Quorvex Sweden AB</div>
      <div>Bruksvägen 14, SE-175 43 JÄRFÄLLA,</div>
      <div>Sweden</div>
      <div class="contact__phones">
        <div><span class="contact__label">Mobile:</span>+46735 21 47 83</div>
        <div><span class="contact__label">Office:</span>+46 8 61 94 27</div>
      </div>
    </div>

    <svg class="footer-band" viewBox="0 0 634 62" aria-hidden="true">
      <path d="M0 6 C 220 -4, 440 4, 597 62 L 570 62 C 430 18, 230 2, 0 10 Z" fill="var(--swoosh-grey)"/>
      <path d="M0 11 C 230 3, 430 18, 590 62 L 0 62 Z" fill="var(--brand-blue)"/>
    </svg>
    <div class="web">www.<strong>quorvex-example</strong>.com</div>
  </section>

  <section class="card card--back">
    <div class="brand-name">QUORVEX</div>
  </section>
</body>
</html>
```